New document sharing business needs snazzy icons

We need two icons designed for a new document sharing business based in Brisbane, Australia. Users of the website can download high quality document templates and examples, or upload content to share with others.
We need two icons to go on the home page that draws attention to the two main functions of the website (download and share). These icons need to be a little different, but consistent in size and general appearance. These icons will hyperlink to the "download" and "upload" pages of the website.
The first icon needs to have the word "Download" as the dominant word. Under or beside this word the following words need to appear: "search and download documents" in smaller writing. The image needs to portray a professional, elegant look whilst being visually appealing. This icon may use the down arrow or some variation to depict the downloading of a document.
The second icon needs to have the word "Share" as the dominant word. Under or beside this word the following words need to appear: "upload your documents to get free downloads" in smaller writing. This icon may use the up arrow or some variation to depict the sharing or uploading of documents.
I would expect that both icons may use different (but complimentary) colours, and be of the same overall size and structure.
Customers are business managers and executives.
Business

```html
<!DOCTYPE html>
<html lang="en">
<head>
<meta charset="utf-8">
<title>Download and Share Buttons</title>
<link rel="stylesheet" href="https://fonts.googleapis.com/css2?family=PT+Sans&display=swap">
<style>
  :root {
    --page-bg: #ffffff;
    --purple-top: #c07fd0; --purple-mid: #8a1fa0; --purple-bottom: #4a0a5e; --purple-edge: #a020c0; --purple-ink: #9b34b3;
    --red-top: #ff8a90; --red-mid: #e0202e; --red-bottom: #9a1420; --red-edge: #d02030; --red-ink: #c81d2a;
    --orange-top: #ffe07a; --orange-mid: #ffa000; --orange-bottom: #ff6a00; --orange-edge: #ff8a10; --orange-ink: #ff8c00;
    --green-top: #bfe09a; --green-mid: #2f9a3a; --green-bottom: #126a2a; --green-edge: #1a7a30; --green-ink: #2a8a3a;
    --blue-top: #9ae4f6; --blue-mid: #1aa6e0; --blue-bottom: #1260c8; --blue-edge: #2a80e0; --blue-ink: #1a9ae0;
    --title-ink: rgba(40, 20, 40, 0.55);
    --subtitle-ink: #ffffff;
  }
  * { margin: 0; padding: 0; box-sizing: border-box; }
  html, body { width: 1200px; height: 1076px; overflow: hidden; background: var(--page-bg); }
  .canvas { position: relative; width: 1200px; height: 1076px; font-family: "PT Sans", sans-serif; }

  .action-button {
    position: absolute; width: 402px; height: 118px; border-radius: 11px; overflow: hidden;
    border: 1.5px solid var(--edge);
    background: linear-gradient(to bottom, var(--mid) 45%, var(--bottom) 100%);
    text-decoration: none; display: block;
  }
  .action-button .gloss { position: absolute; inset: 0; width: 100%; height: 100%; }
  .action-button .title {
    position: absolute; left: 14px; top: 10px; font-size: 66px; line-height: 1;
    color: var(--title-ink); letter-spacing: -1.2px; white-space: nowrap;
  }
  .action-button .subtitle {
    position: absolute; left: 17px; top: 76px; font-size: 19px; color: var(--subtitle-ink); white-space: nowrap;
  }
  .action-button .badge { position: absolute; right: 8px; top: 14px; width: 90px; height: 90px; }

  .is-purple { --top: var(--purple-top); --mid: var(--purple-mid); --bottom: var(--purple-bottom); --edge: var(--purple-edge); --ink: var(--purple-ink); left: 99px; top: 144px; }
  .is-red { --top: var(--red-top); --mid: var(--red-mid); --bottom: var(--red-bottom); --edge: var(--red-edge); --ink: var(--red-ink); left: 99px; top: 372px; }
  .is-orange { --top: var(--orange-top); --mid: var(--orange-mid); --bottom: var(--orange-bottom); --edge: var(--orange-edge); --ink: var(--orange-ink); left: 99px; top: 600px; }
  .is-green { --top: var(--green-top); --mid: var(--green-mid); --bottom: var(--green-bottom); --edge: var(--green-edge); --ink: var(--green-ink); left: 99px; top: 828px; }
  .is-blue { --top: var(--blue-top); --mid: var(--blue-mid); --bottom: var(--blue-bottom); --edge: var(--blue-edge); --ink: var(--blue-ink); left: 697px; top: 486px; }

  .share-button .title { left: 73px; color: rgba(20, 40, 60, 0.55); letter-spacing: -0.8px; }
  .share-button .subtitle { left: 8px; top: 78px; font-size: 14.4px; }
</style>
</head>
<body>
<main class="canvas">

  <a class="action-button is-purple download-button" href="#download">
    <svg class="gloss" viewBox="0 0 402 118" preserveAspectRatio="none" aria-hidden="true">
      <path d="M0,0 H402 V52 Q200,50 0,74 Z" fill="var(--top)"/>
    </svg>
    <span class="title">Download</span>
    <span class="subtitle">search and download documents</span>
    <svg class="badge" viewBox="0 0 90 90" aria-hidden="true">
      <circle cx="45" cy="45" r="44" fill="var(--ink)" opacity="0.6"/>
      <circle cx="45" cy="45" r="36" fill="#fff"/>
      <path d="M31,26 H53 L60,33 V64 H31 Z" fill="none" stroke="var(--ink)" stroke-width="4" stroke-linejoin="round"/>
      <path d="M40,34 H50 V52 H58 L45,66 L32,52 H40 Z" fill="var(--bottom)" stroke="#fff" stroke-width="2"/>
    </svg>
  </a>

  <a class="action-button is-red download-button" href="#download">
    <svg class="gloss" viewBox="0 0 402 118" preserveAspectRatio="none" aria-hidden="true">
      <path d="M0,0 H402 V52 Q200,50 0,74 Z" fill="var(--top)"/>
    </svg>
    <span class="title">Download</span>
    <span class="subtitle">search and download documents</span>
    <svg class="badge" viewBox="0 0 90 90" aria-hidden="true">
      <circle cx="45" cy="45" r="44" fill="var(--ink)" opacity="0.5"/>
      <circle cx="45" cy="45" r="36" fill="#fff"/>
      <path d="M31,26 H53 L60,33 V64 H31 Z" fill="none" stroke="var(--ink)" stroke-width="4" stroke-linejoin="round"/>
      <path d="M40,34 H50 V52 H58 L45,66 L32,52 H40 Z" fill="var(--bottom)" stroke="#fff" stroke-width="2"/>
    </svg>
  </a>

  <a class="action-button is-orange download-button" href="#download">
    <svg class="gloss" viewBox="0 0 402 118" preserveAspectRatio="none" aria-hidden="true">
      <path d="M0,0 H402 V52 Q200,50 0,74 Z" fill="var(--top)"/>
    </svg>
    <span class="title">Download</span>
    <span class="subtitle">search and download documents</span>
    <svg class="badge" viewBox="0 0 90 90" aria-hidden="true">
      <circle cx="45" cy="45" r="44" fill="var(--top)" opacity="0.7"/>
      <circle cx="45" cy="45" r="36" fill="#fff"/>
      <path d="M31,26 H53 L60,33 V64 H31 Z" fill="none" stroke="var(--ink)" stroke-width="4" stroke-linejoin="round"/>
      <path d="M40,34 H50 V52 H58 L45,66 L32,52 H40 Z" fill="var(--bottom)" stroke="#fff" stroke-width="2"/>
    </svg>
  </a>

  <a class="action-button is-green download-button" href="#download">
    <svg class="gloss" viewBox="0 0 402 118" preserveAspectRatio="none" aria-hidden="true">
      <path d="M0,0 H402 V52 Q200,50 0,74 Z" fill="var(--top)"/>
    </svg>
    <span class="title">Download</span>
    <span class="subtitle">search and download documents</span>
    <svg class="badge" viewBox="0 0 90 90" aria-hidden="true">
      <circle cx="45" cy="45" r="44" fill="var(--bottom)" opacity="0.8"/>
      <circle cx="45" cy="45" r="36" fill="#fff"/>
      <path d="M31,26 H53 L60,33 V64 H31 Z" fill="none" stroke="var(--ink)" stroke-width="4" stroke-linejoin="round"/>
      <path d="M40,34 H50 V52 H58 L45,66 L32,52 H40 Z" fill="var(--bottom)" stroke="#fff" stroke-width="2"/>
    </svg>
  </a>

  <a class="action-button is-blue share-button" href="#upload">
    <svg class="gloss" viewBox="0 0 402 118" preserveAspectRatio="none" aria-hidden="true">
      <path d="M0,0 H402 V50 Q200,52 0,72 Z" fill="var(--top)"/>
    </svg>
    <span class="title">Share</span>
    <span class="subtitle">upload your documents to get free downloads</span>
    <svg class="badge" viewBox="0 0 90 90" aria-hidden="true">
      <circle cx="45" cy="45" r="44" fill="var(--bottom)" opacity="0.7"/>
      <circle cx="45" cy="45" r="36" fill="#fff"/>
      <path d="M31,26 H53 L60,33 V64 H31 Z" fill="none" stroke="var(--ink)" stroke-width="4" stroke-linejoin="round"/>
      <path d="M40,62 H50 V44 H58 L45,30 L32,44 H40 Z" fill="var(--bottom)" stroke="#fff" stroke-width="2"/>
    </svg>
  </a>

</main>
</body>
</html>
```